New Business Card Design Project

Use the flyer uploaded and website www.brightoakbuilders.com for inspiration.
List Our Services on Backside of business cards
Martin Hollis
Harborline Renovations Inc.
Licensed General Contractors
858-471-9063

Contact Information for Business Card

Use the flyer uploaded and website www.brightoakbuilders.com for inspiration. List Our Services on Backside of business cards Martin Hollis Harborline Renovations Inc. Licensed General Contractors 858-471-9063

```html
<!DOCTYPE html>
<html lang="en">
<head>
<meta charset="utf-8">
<title>Harborline Renovations – Business Cards</title>
<link rel="stylesheet" href="https://fonts.googleapis.com/css2?family=Montserrat:wght@400;500;700&family=Questrial&display=swap">
<style>
  :root {
    --backdrop: #3a3a3c;
    --card-white: #ffffff;
    --card-black: #1d1d1f;
    --accent-blue: #2f86d6;
    --ink-dark: #1a1a1a;
    --ink-light: #f4f4f4;
  }
  html, body {
    margin: 0;
    width: 1200px;
    height: 1200px;
    overflow: hidden;
    background: var(--backdrop);
  }
  .sheet {
    position: relative;
    width: 1200px;
    height: 1200px;
  }
  .card {
    position: absolute;
    left: 150px;
    width: 900px;
    height: 514px;
    border-radius: 42px;
    overflow: hidden;
    box-shadow: 0 4px 0 var(--accent-blue), 0 18px 30px rgba(0,0,0,0.35);
  }
  .card--front { top: 56px; background: var(--card-white); }
  .card--back  { top: 632px; background: var(--card-black); }

  .front-lower {
    position: absolute;
    left: 0; right: 0;
    top: 268px; bottom: 0;
    background: var(--card-black);
    border-top: 9px solid var(--accent-blue);
    box-shadow: 0 -9px 0 var(--card-white) inset;
  }
  .front-lower::before {
    content: "";
    position: absolute;
    left: 0; right: 0; top: 0;
    height: 10px;
    background: var(--card-white);
  }

  .brand-name {
    position: absolute;
    font-family: "Montserrat", sans-serif;
    font-weight: 500;
    letter-spacing: 0.12em;
    text-transform: uppercase;
    white-space: nowrap;
  }
  .card--front .brand-name {
    left: 0; right: 0;
    top: 118px;
    text-align: center;
    font-size: 40px;
    color: var(--ink-dark);
  }
  .card--back .brand-name {
    left: 0; right: 0;
    top: 232px;
    text-align: center;
    font-size: 46px;
    color: var(--ink-light);
  }

  .person {
    position: absolute;
    left: 70px;
    bottom: 74px;
    font-family: "Montserrat", sans-serif;
  }
  .person__name {
    margin: 0;
    font-size: 46px;
    font-weight: 700;
    color: var(--accent-blue);
    text-transform: uppercase;
    line-height: 1;
  }
  .person__title {
    margin: 8px 0 0 4px;
    font-size: 24px;
    font-weight: 500;
    color: var(--ink-light);
    text-transform: uppercase;
    letter-spacing: 0.02em;
  }

  .contact {
    position: absolute;
    left: 480px;
    top: 318px;
    font-family: "Questrial", sans-serif;
    color: var(--ink-light);
    font-size: 26px;
  }
  .contact__heading { margin: 0 0 10px; font-size: 26px; font-weight: 400; }
  .contact__list { list-style: none; margin: 0; padding: 0 0 0 6px; }
  .contact__item {
    display: flex;
    align-items: center;
    gap: 14px;
    height: 40px;
  }
  .contact__icon { width: 24px; height: 24px; flex: none; }
</style>
</head>
<body>
<main class="sheet">

  <section class="card card--front" aria-label="Business card front">
    <div class="brand-name">Harborline Renovations</div>
    <div class="front-lower"></div>

    <div class="person">
      <h1 class="person__name">Martin Hollis</h1>
      <p class="person__title">Director</p>
    </div>

    <div class="contact">
      <p class="contact__heading">Licensed General Contractors</p>
      <ul class="contact__list">
        <li class="contact__item">
          <svg class="contact__icon" viewBox="0 0 24 24" aria-hidden="true">
            <path fill="var(--accent-blue)" d="M6.6 10.8a15.1 15.1 0 0 0 6.6 6.6l2.2-2.2a1 1 0 0 1 1-.25 11.4 11.4 0 0 0 3.6.57 1 1 0 0 1 1 1V20a1 1 0 0 1-1 1A17 17 0 0 1 3 4a1 1 0 0 1 1-1h3.5a1 1 0 0 1 1 1c0 1.25.2 2.46.57 3.6a1 1 0 0 1-.25 1z"/>
          </svg>
          <span>858-471-9063</span>
        </li>
        <li class="contact__item">
          <svg class="contact__icon" viewBox="0 0 24 24" aria-hidden="true">
            <path fill="none" stroke="var(--accent-blue)" stroke-width="2.4" d="M12 22s-7-7.2-7-12a7 7 0 0 1 14 0c0 4.8-7 12-7 12z"/>
            <circle cx="12" cy="10" r="2.6" fill="var(--accent-blue)"/>
          </svg>
          <span>Harborline Renovations Inc.</span>
        </li>
        <li class="contact__item">
          <svg class="contact__icon" viewBox="0 0 24 24" aria-hidden="true">
            <g fill="none" stroke="var(--accent-blue)" stroke-width="1.8">
              <circle cx="12" cy="12" r="9.5"/>
              <ellipse cx="12" cy="12" rx="4.3" ry="9.5"/>
              <path d="M2.5 12h19M4 7h16M4 17h16"/>
            </g>
          </svg>
          <span>brightoakbuilders.com</span>
        </li>
      </ul>
    </div>
  </section>

  <section class="card card--back" aria-label="Business card back">
    <div class="brand-name">Harborline Renovations</div>
  </section>

</main>
</body>
</html>
```